TRV Medicaid and Estate Planning

Improve look and feel of existing content. Create consistency between website and brochure aesthetics/theme.

The average monthly cost for a nursing home is about $5,000. Most people cannot afford that. As a result, roughly 65% of all nursing home residents turn to Medicaid to finance their medical care. Medicaid is a state and federally funded Title 19 benefit program, and most people recognize Medicaid as a program to help poor people. But, fewer people recognize Medicaid as a program that can help most middle class families to preserve their wealth and even pass an inheritance—all the while receiving Medicaid benefits to cover the costs of long term care.

Marcus L. Doyle
Texas
mdoyle@trvlawgroup.example
(555) 248-3071 x204
Due to a lack of understanding or possibly a stigmatization of “receiving benefits,” a lot of families pay the nursing home from their life savings. But $60,000 a year as a private pay patient will quickly expend most people’s life savings. The next step is usually to sell the family home to continue paying privately. The hard truth is none of that is necessary with proper Medicaid planning. An unfortunate reality is that a great number of families who could have benefitted from Medicaid planning will eventually end up turning to Medicaid when they have exhausted all other resources.

But wouldn’t it be nice to pass an inheritance to the grandchildren? Or, to provide for a special needs child? What about preserving the life savings entirely? These are some of the things an elder law attorney can help with. The Medicaid qualification criteria and its governing law is complex, but it was written with numerous provisions that allow for the protection of the family.

Seventy percent of those over 65 years old will need some form of long term care in their lifetimes. If you or someone you love is within that 70%, consult with an elder law attorney to see what planning options you may have.

Don’t Go Bankrupt Paying a Nursing Home

If your loved one needs long term care, but you cannot afford the cost of a nursing home, what do you do? People all across Texas are asking themselves this same question. The number one payer source for long term care is Medicaid—not long term care insurance, not Medicare, not life savings. So, the question is: are you eligible for nursing home Medicaid?

For a free legal consultation, contact us at (555) 613-8842 or mdoyle@trvlawgroup.example.

http://www.trvlawgroup.example/estate-planning/medicaid-nursing-homes-and-estate-planning/

Target Market(s)

Texas, Colorado, Elder Law and Estate Planning interests

Font styles to use
Serif

Requirements
Must have
• content I submitted

```html
<!DOCTYPE html>
<html lang="en">
<head>
<meta charset="utf-8">
<title>Trevino, Rourke &amp; Vance — Medicaid, Nursing Homes &amp; Estate Planning</title>
<link rel="stylesheet" href="https://fonts.googleapis.com/css2?family=Cinzel:wght@400;500&family=Libre+Caslon+Text&family=Open+Sans:wght@400;600&display=swap">
<style>
  :root {
    --ink-dark: #1c1c1c;
    --ink-mid: #2a2a2a;
    --ink-soft: #3a3a3a;
    --paper: #ffffff;
    --title-grey: #d8d8d8;
    --sub-grey: #9a9a9a;
    --rule-grey: #4a4a4a;
    --accent-orange: #e36f2b;
    --accent-green: #17402a;
    --accent-tan: #c9b98a;
    --accent-gold: #f2a531;
    --accent-navy: #1b2b5a;
  }
  html, body {
    margin: 0;
    padding: 0;
    width: 1200px;
    height: 927px;
    overflow: hidden;
    background: var(--ink-dark);
  }
  .brochure {
    position: relative;
    width: 1200px;
    height: 927px;
    overflow: hidden;
    color: var(--paper);
    font-family: "Open Sans", Arial, sans-serif;
  }
  .backdrop {
    position: absolute;
    inset: 0;
    background:
      radial-gradient(ellipse 60% 45% at 30% 55%, rgba(120,120,120,.28), transparent 70%),
      radial-gradient(ellipse 40% 30% at 75% 40%, rgba(100,100,100,.22), transparent 70%),
      linear-gradient(180deg, #2c2c2c 0%, #262626 20%, #1e1e1e 50%, #0e0e0e 72%, #222 76%, #2a2a2a 100%);
  }
  .firm-name {
    position: absolute;
    top: 38px;
    left: 0;
    width: 1200px;
    margin: 0;
    text-align: center;
    font-family: "Cinzel", "Times New Roman", serif;
    font-weight: 400;
    font-size: 54px;
    letter-spacing: 1px;
    line-height: 1;
    color: var(--title-grey);
  }
  .firm-tagline {
    position: absolute;
    top: 102px;
    left: 0;
    width: 1200px;
    margin: 0;
    text-align: center;
    font-family: "Cinzel", "Times New Roman", serif;
    font-size: 36px;
    letter-spacing: 1px;
    line-height: 1;
    color: var(--sub-grey);
  }
  .accent-rule {
    position: absolute;
    left: 0;
    width: 1200px;
    height: 5px;
  }
  .accent-rule--top { top: 188px; }
  .accent-rule--bottom { top: 697px; }
  .section-title {
    position: absolute;
    top: 226px;
    left: 0;
    width: 1200px;
    margin: 0;
    text-align: center;
    font-family: "Libre Caslon Text", "Times New Roman", serif;
    font-weight: 400;
    font-size: 25px;
    letter-spacing: .5px;
    color: var(--sub-grey);
  }
  .column {
    position: absolute;
    top: 272px;
    width: 316px;
    font-weight: 600;
    font-size: 16px;
    line-height: 23.2px;
    text-align: justify;
    hyphens: auto;
  }
  .column p { margin: 0 0 8px; }
  .column--one { left: 42px; }
  .column--two { left: 442px; }
  .column--three { left: 842px; }
  .info-block {
    position: absolute;
    top: 728px;
    font-size: 16px;
    line-height: 22px;
  }
  .info-block h2 {
    margin: 0 0 4px;
    font-family: "Libre Caslon Text", "Times New Roman", serif;
    font-weight: 400;
    font-size: 20px;
    line-height: 28px;
  }
  .info-block p { margin: 0; text-align: justify; }
  .info-block--planning { left: 42px; width: 316px; }
  .info-block--qualify { left: 432px; width: 316px; }
  .criteria { list-style: none; margin: 0; padding: 0; }
  .criteria-continued {
    position: absolute;
    top: 760px;
    left: 842px;
    width: 316px;
    list-style: none;
    margin: 0;
    padding: 0;
    font-size: 16px;
    line-height: 22px;
  }
</style>
</head>
<body>
<main class="brochure">
  <div class="backdrop" role="img" aria-label="Dim black and white photograph of a pen resting on paperwork"></div>

  <h1 class="firm-name">TREVINO, ROURKE &amp; VANCE</h1>
  <p class="firm-tagline">ATTORNEYS AT LAW</p>

  <svg class="accent-rule accent-rule--top" viewBox="0 0 1200 5" preserveAspectRatio="none" aria-hidden="true">
    <rect x="0" y="0" width="1200" height="5" fill="var(--rule-grey)"/>
    <rect x="157" y="0" width="177" height="5" fill="var(--accent-orange)"/>
    <rect x="334" y="0" width="177" height="5" fill="var(--accent-green)"/>
    <rect x="511" y="0" width="178" height="5" fill="var(--accent-tan)"/>
    <rect x="689" y="0" width="177" height="5" fill="var(--accent-gold)"/>
    <rect x="866" y="0" width="177" height="5" fill="var(--accent-navy)"/>
  </svg>

  <h2 class="section-title">MEDICAID, NURSING HOMES &amp; ESTATE PLANNING</h2>

  <section class="column column--one">
    <p>The average monthly cost for a nursing home is about $5,000.</p>
    <p>Most people cannot afford that. As a result, roughly 65% of all nursing home residents turn to Medicaid to finance their medical care. Medicaid is a state and federally funded Title 19 benefit program, and most people recognize Medicaid as a program to help poor people. But, fewer people recognize Medicaid as a program that can help most middle class families to preserve their wealth and even pass an inheritance—all the while receiving Medicaid benefits to cover the costs of long term care.</p>
  </section>

  <section class="column column--two">
    <p>Due to a lack of understanding or possibly a stigmatization of “receiving benefits,” a lot of families pay the nursing home from their life savings. But $60,000 a year as a private pay patient will quickly expend most people’s life savings. The next step is usually to sell the family home to continue paying privately. The hard truth is none of that is necessary with proper Medicaid planning. An unfortunate reality is that a great number of families who could have benefitted from Medicaid planning will eventually end up turning to Medicaid when they have exhausted all other resources.</p>
  </section>

  <section class="column column--three">
    <p>But wouldn’t it be nice to pass an inheritance to the grandchildren? Or, to provide for a special needs child? What about preserving the life savings entirely? These are some of the things an elder law attorney can help with. The Medicaid qualification criteria and its governing law is complex, but it was written with numerous provisions that allow for the protection of the family.</p>
    <p>Seventy percent of those over 65 years old will need some form of long term care in their lifetimes. If you or someone you love is within that 70%, consult with an elder law attorney to see what planning options you may have.</p>
  </section>

  <svg class="accent-rule accent-rule--bottom" viewBox="0 0 1200 5" preserveAspectRatio="none" aria-hidden="true">
    <rect x="0" y="0" width="1200" height="5" fill="var(--rule-grey)"/>
    <rect x="157" y="0" width="177" height="5" fill="var(--accent-orange)"/>
    <rect x="334" y="0" width="177" height="5" fill="var(--accent-green)"/>
    <rect x="511" y="0" width="178" height="5" fill="var(--accent-tan)"/>
    <rect x="689" y="0" width="177" height="5" fill="var(--accent-gold)"/>
    <rect x="866" y="0" width="177" height="5" fill="var(--accent-navy)"/>
  </svg>

  <section class="info-block info-block--planning">
    <h2>What Is Medicaid Planning?</h2>
    <p>Medicaid Planning usually involves restructuring assets to meet federal and state law eligibility criteria so that your loved one can get the medical care he or she needs and deserves.</p>
  </section>

  <section class="info-block info-block--qualify">
    <h2>How Do You Qualify for Medicaid?</h2>
    <p>Generally speaking, only seven qualification rules exist. A Nursing Home Medicaid Applicant must:</p>
    <ol class="criteria">
      <li>1) be a resident of Texas</li>
      <li>2) be a citizen of the United States</li>
      <li>3) be at least 65 years old or disabled</li>
    </ol>
  </section>

  <ol class="criteria-continued">
    <li>4) be in a skilled nursing facility for 30 days</li>
    <li>5) have a medical necessity for long term care</li>
    <li>6) have less than $2,205 gross monthly income</li>
  </ol>
</main>
</body>
</html>
```